E-Book-Cover für meinen Roman Was der Nebel trägt
Sehr angenehmer Kontakt, das Beschriebene wurde auf Anhieb in die Richtung umgesetzt, die ich angestrebt habe. Änderungswünsche wurden prompt und unermüdlich umgesetzt, bis das Endergebnis stand. Sehr zu empfehlen!
Zielgruppe
Ich veröffentliche in Eigenregie meinen Roman namens 'Was der Nebel trägt' im Rahmen des Self-Publishing Angebots von Lesowa.de
Bei meinem Werk handelt es sich um Belletristik: eine Geschichte aus dem Leben, die traurige und lustige Elemente zu gleichen Teilen eint. Behandelt wird der Lebensabschnitt eines Jugendlichen, der zu früh Erfahrung mit dem Tod macht, als seine Mutter schwer erkrankt. Gleichzeitig gilt es, den (humorvoll verpackten) Alltag zu meistern, in dem er wieder und wieder auf Ablehnung und Distanz angesichts seiner ungewöhnlichen und misslichen Lage stößt. Es gelingt ihm nicht mehr, Teil seiner gleichaltrigen Mitstreiter zu werden.
Gleichzeitig gibt es einen zweiten Handlungsstrang, in dem eine ebenfalls Jugendliche ähnliche Erfahrungen macht, auch wenn die Umstände andere sind, ebenso wie die Reaktion darauf. Während der männliche Protagonist wiederholt von seinem Umkreis enttäuscht wird, stellt er sich am Ende der Prüfung, der er nicht entkommen kann. Sein weibliches Pendant hingegen tritt eine überstürzte Flucht mit ungewissem Ausgang an. Beide Stränge sind lose miteinander verwoben, und als Leser stellt man sich zusehends die Frage, ob und wann diese verbunden werden. Eine Auflösung erfolgt am Schluss.
Nach einigen Testlesern stellte sich heraus, dass jene am meisten begeistert waren, die selbst ähnliche Erfahrungen gemacht haben, wie die fiktiven Personen. Grundsätzlich lässt sich aber sagen, dass der Schreibstil, die beschriebenen Medien und Situationen eher auf (junge) Erwachsene zugeschnitten sind. Dennoch handelt es sich nicht um ein klassisches Jugendbuch, oft werden Dinge beschrieben, die für Minderjährige nicht geeignet sind. Als (Haupt)zielgruppe würde ich grob den Rahmen 20-40 Jahre vorgeben, wobei die Leser eher noch älter als jünger sein dürfen.
Aufgabenstellung
Zunächst technisch: (Angaben lt. Lesowa)
JPEG oder TIFF-Datei
mindestens 1000 Pixel an der längsten Seite
Idealverhältnis von Bildhöhe- und breite: 1,6 (Beispiel: 1000 x 1600)
bei weißen Covern sollte ein 2-3 Pixel breiter, grauer Rand hinzugefügt werden, damit sich das Cover von der Website selbst abhebt
Weiterhin zu beachten:
-Hauptsächlich wird es auf eBook Readern gelesen, die nur in Graustufen darstellen. Das Cover sollte also in jedem Fall auch in Schwarz-Weiß nichts von seiner Wirkung einbüßen!
Selbiges gilt für eine Miniaturansicht!
Autor: Matthias Krollner
Titel: Was der Nebel trägt
Zusatz: Roman
Nun zu den wichtigsten Vorgaben:
-Selbstverständlich soll das Cover Aufmerksamkeit erzeugen und neugierig machen.
-Das Thema "anders sein" / "im Abseits stehen" / "hin- und hergetrieben werden" muss auf jeden Fall rübergebracht werden, da dies auch das Kernthema des Buches ist.
-Bei der Schriftart gibt es keine bestimmte Vorgabe, nur bitte nichts in Kapitälchen oder Großbuchstaben. (z.B. WAS DER NEBEL TRÄGT)
-Es soll auf keinen Fall übertrieben ernst oder möchtegern-schnulzig rüberkommen. (Bilder vom Strand, untergehender Sonne und weitere Klischees.)
-Vielmehr darf man dem Cover bereits ansehen, dass es ein ernstes Thema auch mit Humor nehmen kann. z.B. durch Stilisierung, einfache Farben anstatt aufwändiger Realaufnahmen und Schatten, evtl. auch in Richtung Comic, aber nicht zu albern.
-Die Platzierung von Autor und Titel darf klassisch sein, gerne aber auch ungewöhnlich überraschend.
Ich habe diesem Inserat einige Entwürfe meinerseits beigefügt, wie ich das o.g. Thema stilisieren würde, z.B.:
der Querschnitt eines einfahrenden Zuges (Hauptverkehrsmittel im Buch), bei dem in allen Fenstern Licht brennt, mit Ausnahme von einem. (Hier dürfen gerne auch die Profile von Menschen hinzug..

```html
<!DOCTYPE html>
<html lang="de">
<head>
<meta charset="utf-8">
<title>Was der Nebel trägt – Matthias Krollner</title>
<link rel="stylesheet" href="https://fonts.googleapis.com/css2?family=Exo+2:wght@500;700;800&display=swap">
<style>
  :root {
    --page: #ffffff;
    --frame: #d9d9d9;
    --cover: #ffffff;
    --red: #dd574a;
    --salmon: #e8968a;
    --rose: #edb8c0;
    --lavender: #a5a1cf;
    --ink: #111111;
    --track: #9a9a9a;
  }
  * { margin: 0; padding: 0; box-sizing: border-box; }
  html, body {
    width: 885px;
    height: 1200px;
    overflow: hidden;
    background: var(--page);
  }
  .cover {
    position: absolute;
    left: 148px;
    top: 134px;
    width: 586px;
    height: 938px;
    background: var(--cover);
    border: 6px solid var(--frame);
    box-shadow: 1px 2px 2px rgba(0,0,0,0.12);
    overflow: hidden;
    font-family: "Exo 2", "Arial Narrow", sans-serif;
  }
  .cover-art {
    position: absolute;
    left: 0;
    top: 0;
    width: 100%;
    height: 560px;
  }
  .title {
    position: absolute;
    left: 0;
    width: 100%;
    text-align: center;
    font-weight: 800;
    line-height: 1;
    letter-spacing: -0.5px;
  }
  .title-line { position: absolute; left: 0; width: 100%; }
  .title-line--small { color: var(--red); font-size: 66px; }
  .title-line--large { color: var(--lavender); font-size: 94px; }
  .title-line--1 { top: 458px; }
  .title-line--2 { top: 524px; }
  .title-line--3 { top: 574px; }
  .title-line--4 { top: 662px; }
  .genre {
    position: absolute;
    top: 751px;
    left: 0;
    width: 100%;
    text-align: center;
    color: var(--red);
    font-weight: 700;
    font-size: 21px;
  }
  .author {
    position: absolute;
    top: 803px;
    left: 0;
    width: 100%;
    text-align: center;
    color: var(--ink);
    font-weight: 500;
    font-size: 30px;
    letter-spacing: 0.3px;
  }
</style>
</head>
<body>
  <main class="cover">
    <svg class="cover-art" viewBox="0 0 574 560" preserveAspectRatio="none"
         role="img" aria-label="Gezeichnete Bahnstrecke mit Oberleitungen, die in die Ferne führt, eine einsame Gestalt auf den Gleisen, roter Himmel über flacher Landschaft">
      <defs>
        <linearGradient id="landscape" x1="0" y1="0" x2="0" y2="1">
          <stop offset="0" stop-color="#ffffff"/>
          <stop offset="0.18" stop-color="#ffffff"/>
          <stop offset="0.26" stop-color="#dd574a"/>
          <stop offset="0.72" stop-color="#dd574a"/>
          <stop offset="0.78" stop-color="#e8968a"/>
          <stop offset="0.86" stop-color="#edb8c0"/>
          <stop offset="0.92" stop-color="#a5a1cf"/>
          <stop offset="1" stop-color="#d6d4e8"/>
        </linearGradient>
        <linearGradient id="fade" x1="0" y1="0" x2="0" y2="1">
          <stop offset="0.45" stop-color="#ffffff" stop-opacity="0"/>
          <stop offset="1" stop-color="#ffffff" stop-opacity="1"/>
        </linearGradient>
      </defs>
      <rect x="0" y="0" width="574" height="340" fill="url(#landscape)"/>
      <rect x="0" y="340" width="574" height="220" fill="#cfcfd6"/>
      <rect x="0" y="340" width="574" height="220" fill="url(#fade)"/>
    </svg>

    <h1 class="title">
      <span class="title-line title-line--small title-line--1">Was</span>
      <span class="title-line title-line--small title-line--2">der</span>
      <span class="title-line title-line--large title-line--3">Nebel</span>
      <span class="title-line title-line--small title-line--4">trägt</span>
    </h1>
    <p class="genre">Roman</p>
    <p class="author">Matthias Krollner</p>
  </main>
</body>
</html>
```